New Business Cards for Organic Meat Farm

We need a business card designed for Quillbrook Farm, a meat farm in western MA. Our logo uses a hand-drawn woodcut (attached). Our color palette has been simply black and white (shown in notepad and picture of our food truck). While we are based out of western MA, we have ambitions to grow nationally, so our hope is for a classy and memorable card which will be printed on a premium quality stock from a printer like printkestrel.com.
Target Market(s)
consumers of quality meats, restauranteurs, partnering farms
Industry/Entity Type
Farming and prepared meat products
Contact Information for Business Card
Dorian Vessick, President/Owner, dorian@quillbrookfarm.com, mobile: 413-555-0172, phone: 413-555-0148, quillbrookfarm.com, facebook: @quillbrookfarm, instagram: @quillbrookfarmma
Colors
Designer to choose colors to be used in the design.
Look and feel

```html
<!DOCTYPE html>
<html lang="en">
<head>
<meta charset="utf-8">
<title>Quillbrook Farm – Business Card</title>
<link rel="stylesheet" href="https://fonts.googleapis.com/css2?family=Marcellus&family=Poppins:wght@300;400&display=swap">
<style>
  :root {
    --backdrop: #bfc3c8;
    --card: #151516;
    --ink: #f4f4f4;
    --ink-soft: #e0e0e0;
    --silver-light: #f4f4f4;
    --silver-dark: #5b5b5b;
  }
  * { margin: 0; padding: 0; box-sizing: border-box; }
  html, body { width: 1200px; height: 1112px; overflow: hidden; background: var(--backdrop); }
  .canvas { position: relative; width: 1200px; height: 1112px; }
  .card {
    position: absolute; width: 753px; height: 442px;
    background: var(--card); overflow: hidden; color: var(--ink);
  }
  .card--front { left: 73px; top: 75px; }
  .card--back { left: 372px; top: 592px; }
  .card__decor { position: absolute; inset: 0; width: 100%; height: 100%; }

  .brand-name {
    position: absolute; left: 0; right: 0; top: 186px;
    text-align: center;
    font-family: "Marcellus", serif; font-weight: 400; font-size: 46px; letter-spacing: 1px;
    color: var(--ink);
  }

  .holder { position: absolute; left: 52px; top: 52px; }
  .holder__name {
    font-family: "Marcellus", serif; font-weight: 400; font-size: 50px; line-height: 1;
    color: var(--ink);
  }
  .holder__title {
    margin-top: 10px;
    font-family: "Poppins", sans-serif; font-weight: 300; font-size: 20px; color: var(--ink-soft);
  }
  .holder__rule {
    position: absolute; left: 52px; top: 155px; width: 100px; height: 2px;
    background: linear-gradient(90deg, var(--silver-light), rgba(255,255,255,0));
  }

  .contact-list { position: absolute; left: 50px; top: 196px; list-style: none; }
  .contact-list__item { display: flex; align-items: center; height: 36px; margin-bottom: 20.5px; }
  .contact-list__icon {
    width: 36px; height: 36px; border-radius: 50%;
    background: radial-gradient(circle at 30% 25%, var(--silver-light), var(--silver-dark) 95%);
    display: flex; align-items: center; justify-content: center;
  }
  .contact-list__icon svg { width: 18px; height: 18px; }
  .contact-list__text {
    margin-left: 23px;
    font-family: "Poppins", sans-serif; font-weight: 300; font-size: 23px; color: var(--ink); letter-spacing: .3px;
  }

  .social-list { position: absolute; left: 535px; top: 60px; list-style: none; }
  .social-list__item { display: flex; align-items: center; height: 26px; margin-bottom: 11px; }
  .social-list__dot { width: 14px; height: 14px; border: 1.5px solid var(--ink); border-radius: 50%; margin-right: 12px; }
  .social-list__text { font-family: "Poppins", sans-serif; font-weight: 400; font-size: 17px; color: var(--ink); }
</style>
</head>
<body>
<div class="canvas">

  <section class="card card--front">
    <svg class="card__decor" viewBox="0 0 1004 590" preserveAspectRatio="none" aria-hidden="true">
      <defs>
        <radialGradient id="frontGlowTop" cx="443" cy="0" r="260" gradientUnits="userSpaceOnUse">
          <stop offset="0" stop-color="#fff" stop-opacity=".28"/>
          <stop offset="1" stop-color="#fff" stop-opacity="0"/>
        </radialGradient>
        <radialGradient id="frontGlowBottom" cx="860" cy="590" r="260" gradientUnits="userSpaceOnUse">
          <stop offset="0" stop-color="#fff" stop-opacity=".22"/>
          <stop offset="1" stop-color="#fff" stop-opacity="0"/>
        </radialGradient>
      </defs>
      <rect width="1004" height="590" fill="url(#frontGlowTop)"/>
      <rect width="1004" height="590" fill="url(#frontGlowBottom)"/>
      <g stroke="#d8d8d8" stroke-width="2" fill="none">
        <line x1="0" y1="140" x2="118" y2="22" stroke-opacity=".8"/>
        <line x1="0" y1="287" x2="265" y2="22" stroke-opacity=".8"/>
        <line x1="103" y1="0" x2="303" y2="200" stroke-opacity=".55"/>
        <line x1="683" y1="590" x2="845" y2="428" stroke-opacity=".7"/>
        <line x1="753" y1="590" x2="958" y2="385" stroke-opacity=".9"/>
      </g>
    </svg>
    <div class="brand-name">Quillbrook Farm</div>
  </section>

  <section class="card card--back">
    <svg class="card__decor" viewBox="0 0 1004 590" preserveAspectRatio="none" aria-hidden="true">
      <defs>
        <radialGradient id="backGlowTop" cx="214" cy="0" r="260" gradientUnits="userSpaceOnUse">
          <stop offset="0" stop-color="#fff" stop-opacity=".25"/>
          <stop offset="1" stop-color="#fff" stop-opacity="0"/>
        </radialGradient>
        <radialGradient id="backGlowBottom" cx="384" cy="590" r="240" gradientUnits="userSpaceOnUse">
          <stop offset="0" stop-color="#fff" stop-opacity=".22"/>
          <stop offset="1" stop-color="#fff" stop-opacity="0"/>
        </radialGradient>
      </defs>
      <rect width="1004" height="590" fill="url(#backGlowTop)"/>
      <rect width="1004" height="590" fill="url(#backGlowBottom)"/>
      <g stroke="#d8d8d8" stroke-width="2" fill="none">
        <line x1="0" y1="95" x2="95" y2="0" stroke-opacity=".75"/>
        <line x1="90" y1="72" x2="168" y2="0" stroke-opacity=".55"/>
        <line x1="1004" y1="280" x2="714" y2="570" stroke-opacity=".9"/>
        <line x1="1004" y1="425" x2="864" y2="565" stroke-opacity=".9"/>
        <line x1="674" y1="390" x2="879" y2="590" stroke-opacity=".6"/>
      </g>
    </svg>

    <header class="holder">
      <h1 class="holder__name">Dorian Vessick</h1>
      <p class="holder__title">President / Owner</p>
    </header>
    <div class="holder__rule"></div>

    <ul class="contact-list">
      <li class="contact-list__item">
        <span class="contact-list__icon"><svg viewBox="0 0 24 24"><rect x="7" y="2" width="10" height="20" rx="2" fill="none" stroke="#fff" stroke-width="2"/><line x1="10" y1="18" x2="14" y2="18" stroke="#fff" stroke-width="2"/></svg></span>
        <span class="contact-list__text">413-555-0172</span>
      </li>
      <li class="contact-list__item">
        <span class="contact-list__icon"><svg viewBox="0 0 24 24"><path d="M6 3l3 0 2 5-2 1.5c1 2.5 3 4.5 5.5 5.5L16 13l5 2v3c0 1.5-1 2.5-2.5 2.5C10 20 4 14 3.5 5.5 3.5 4 4.5 3 6 3z" fill="#fff"/></svg></span>
        <span class="contact-list__text">413-555-0148</span>
      </li>
      <li class="contact-list__item">
        <span class="contact-list__icon"><svg viewBox="0 0 24 24"><rect x="3" y="6" width="18" height="12" rx="1.5" fill="#fff"/><path d="M3.5 7l8.5 6 8.5-6" fill="none" stroke="#777" stroke-width="1.5"/></svg></span>
        <span class="contact-list__text">dorian@quillbrookfarm.com</span>
      </li>
      <li class="contact-list__item">
        <span class="contact-list__icon"><svg viewBox="0 0 24 24" fill="none" stroke="#fff" stroke-width="1.6"><circle cx="12" cy="12" r="9"/><ellipse cx="12" cy="12" rx="4" ry="9"/><line x1="3" y1="12" x2="21" y2="12"/><line x1="4.5" y1="7.5" x2="19.5" y2="7.5"/><line x1="4.5" y1="16.5" x2="19.5" y2="16.5"/></svg></span>
        <span class="contact-list__text">quillbrookfarm.com</span>
      </li>
    </ul>

    <ul class="social-list">
      <li class="social-list__item"><span class="social-list__dot"></span><span class="social-list__text">@quillbrookfarm</span></li>
      <li class="social-list__item"><span class="social-list__dot"></span><span class="social-list__text">@quillbrookfarmma</span></li>
    </ul>
  </section>

</div>
</body>
</html>
```